Real Estate Sign - For Sale Yard Sign - Bellwether Estates

Our real estate company is looking for a new sign design to hang from in post in the front yard of the homes we are selling. Our company name is Bellwether Estates and we are open to any ideas. Attached for you is our company logo and name. The font is Trajan Pro. We are looking for a classy sign to put in front of our high end more expensive homes. You can either choose to include or not include the words "FOR SALE" on the sign (in our state, only about 1/2 of the real estate signs have room for those words. It is implied with a sign in the yard in front of a home). Thank you.

24 inches wide is important. and the height should be either 18, 24 or 30 inches. For printing purposes either of those heights will work. 18 inches is common, but some signs look great that are taller too. I'm open.

If you have any ideas for some better text options, styles or fonts, feel free to play with it.

P.S. Please feel free to play with the colors. We are not at this point set on a particular color scheme. Colors we think are nice but you may have other better ideas are black, red, white, gold, green

Target Market(s)

High end real estate home owners who choose to use our company to sell their home.

Industry/Entity Type

Real Estate

Requirements
Must have
• Company Logo
Company Name (Bellwether Estates)
Thaddeus Vornholt (please include my name as I am the real estate agent)
503-618-2940 (my phone number for potential clients to contact me)
Website name - bellwetherestatesnw.example
***You can either choose to include the words "FOR SALE" or not***

Dimensions must be 24 inches wide. Height can be either 18, 24 or 30 inches. Must be one of those 3 heights for printing purposes.

```html
<!DOCTYPE html>
<html lang="en">
<head>
<meta charset="utf-8">
<title>Bellwether Estates – For Sale Yard Sign</title>
<link rel="stylesheet" href="https://fonts.googleapis.com/css2?family=Cinzel:wght@400;600&family=Marcellus&family=Great+Vibes&display=swap">
<style>
  :root {
    --paper: #ffffff;
    --ink: #111111;
    --sign-black: #000000;
    --sign-red: #e8212b;
    --silver-light: #f2f2f2;
    --silver-mid: #b9b9b9;
    --silver-dark: #6d6d6d;
    --hairline: #9a9a9a;
  }
  * { margin: 0; padding: 0; box-sizing: border-box; }
  html, body {
    width: 1049px; height: 1200px; overflow: hidden;
    background: var(--paper);
  }
  .sign {
    position: relative;
    width: 1049px; height: 1200px;
    overflow: hidden;
    background: var(--paper);
  }
  .sign__art { position: absolute; inset: 0; }
  .texture-panel {
    position: absolute;
    left: 81px; top: 234px; width: 696px; height: 540px;
    background:
      radial-gradient(ellipse at 30% 75%, rgba(255,255,255,0.55), rgba(255,255,255,0) 55%),
      linear-gradient(160deg, #cfcfcf 0%, #9b9b9b 45%, #b5b5b5 70%, #8a8a8a 100%);
  }
  .contact-panel {
    position: absolute;
    left: 81px; top: 774px; width: 696px; height: 390px;
    background: var(--sign-black);
  }
  .brand {
    position: absolute;
    left: 120px; top: 110px; width: 810px;
    text-align: center;
    font-family: "Cinzel", serif;
    font-weight: 400;
    font-size: 66px;
    line-height: 1.05;
    color: var(--ink);
    letter-spacing: 1px;
  }
  .agent {
    position: absolute;
    left: 81px; top: 464px; width: 696px;
    text-align: center;
    font-family: "Cinzel", serif;
    font-weight: 600;
    color: var(--ink);
  }
  .agent__name { font-size: 62px; line-height: 1; letter-spacing: 1px; }
  .agent__role { font-size: 48px; line-height: 1.1; margin-top: 8px; }
  .contact {
    position: absolute;
    left: 81px; top: 778px; width: 696px;
    text-align: center;
    color: var(--paper);
  }
  .contact__phone {
    font-family: "Marcellus", serif;
    font-size: 104px; line-height: 1.05;
    letter-spacing: 1px;
  }
  .contact__web {
    font-family: "Cinzel", serif;
    font-size: 28px; letter-spacing: 1.5px;
    margin-top: 22px;
  }
  .contact__rule {
    width: 632px; height: 2px; margin: 28px auto 0;
    background: linear-gradient(90deg, rgba(255,255,255,0), #fff 40%, #fff 60%, rgba(255,255,255,0));
  }
  .contact__tagline {
    font-family: "Great Vibes", cursive;
    font-size: 58px; line-height: 1.15;
    margin-top: 18px;
  }
</style>
</head>
<body>
<main class="sign">
  <svg class="sign__art" width="1049" height="1200" viewBox="0 0 1049 1200" aria-hidden="true">
    <defs>
      <linearGradient id="silverFrame" x1="0" y1="0" x2="1" y2="1">
        <stop offset="0" stop-color="#4a4a4a"/>
        <stop offset="0.35" stop-color="#d6d6d6"/>
        <stop offset="0.7" stop-color="#7a7a7a"/>
        <stop offset="1" stop-color="#cfcfcf"/>
      </linearGradient>
      <linearGradient id="silverText" x1="0" y1="0" x2="1" y2="0">
        <stop offset="0" stop-color="#8c8c8c"/>
        <stop offset="0.45" stop-color="#f4f4f4"/>
        <stop offset="0.6" stop-color="#bdbdbd"/>
        <stop offset="1" stop-color="#ededed"/>
      </linearGradient>
      <linearGradient id="ovalRim" x1="0" y1="0" x2="1" y2="1">
        <stop offset="0" stop-color="#9a9a9a"/>
        <stop offset="0.5" stop-color="#1a1a1a"/>
        <stop offset="1" stop-color="#000"/>
      </linearGradient>
    </defs>
    <rect class="outer-border" x="50.5" y="22.5" width="951" height="1200" fill="none" stroke="var(--hairline)" stroke-width="1"/>
    <rect class="panel-frame" x="66" y="206" width="921" height="1010" fill="url(#silverFrame)"/>
    <rect x="77" y="220" width="899" height="990" fill="var(--sign-black)"/>
  </svg>

  <div class="texture-panel" role="img" aria-label="Fine silver string-line pattern backdrop"></div>
  <div class="contact-panel"></div>

  <svg class="sign__art" width="1049" height="1200" viewBox="0 0 1049 1200" aria-hidden="true">
    <rect class="sale-band" x="777" y="216" width="189" height="948" fill="var(--sign-red)"/>
    <ellipse cx="525" cy="216" rx="408" ry="140" fill="url(#ovalRim)"/>
    <ellipse cx="525" cy="212" rx="396" ry="130" fill="var(--paper)"/>
    <ellipse cx="525" cy="212" rx="396" ry="130" fill="none" stroke="#cfcfcf" stroke-width="2"/>
  </svg>

  <svg class="sign__art" width="1049" height="1200" viewBox="0 0 1049 1200">
    <text class="sale-label" transform="translate(926 1134) rotate(-90)"
          font-family="Marcellus, serif" font-size="150" fill="url(#silverText)"
          stroke="#8a8a8a" stroke-width="1" textLength="774" lengthAdjust="spacingAndGlyphs">FOR SALE</text>
  </svg>

  <div class="brand">BELLWETHER<br>ESTATES</div>

  <div class="agent">
    <div class="agent__name">THADDEUS VORNHOLT</div>
    <div class="agent__role">AGENT</div>
  </div>

  <div class="contact">
    <div class="contact__phone">503-618-2940</div>
    <div class="contact__web">BELLWETHERESTATESNW.EXAMPLE</div>
    <div class="contact__rule"></div>
    <div class="contact__tagline">Helping you realize<br>your dream</div>
  </div>
</main>
</body>
</html>
```